Annoucement Design for Pilot Grants

I am looking for an announcement/flyer design for our Pilot Grant Application announcement for next year. Our pilot grant information is housed here: https://portal.sci.norvale.edu/cellmarkers/research/seed-awards/.

I would like an announcement/flyer that I can use to post around campus, but also one that can be used via email with links to the pilot grant page for people to submit applications. There are three pilot grants that will all be announced at the same time next year on September 17, 2018. The deadline for applications will be October 31, 2018 and the funding period will be from November 12th, 2018 - November 11, 2019. I would like to also use this announcement on Twitter and Facebook.

Target Market(s)

Scientist

Colors

Designer to choose colors to be used in the design.

Requirements
Must have
• Epigenetics Logo
• Link to Pilot Grant website and QR code if possible
• Formatted to send via email, twitter and facebook

```html
<!DOCTYPE html>
<html lang="en">
<head>
<meta charset="utf-8">
<title>Seed Award Application Announcement 2018</title>
<link rel="stylesheet" href="https://fonts.googleapis.com/css2?family=Montserrat:wght@200;300;400;600;700;800&family=Lato:wght@400&family=Oswald:wght@300&display=swap">
<style>
  :root {
    --red: #d0202e;
    --ink: #3a3a3c;
    --slate: #555557;
    --quote-grey: #d5cfcf;
    --blue-deep: #124a8c;
    --blue-mid: #2a6fb0;
    --paper: #ffffff;
    --stage: #e8eaed;
    --silver: #b9bcc0;
  }
  * { margin: 0; padding: 0; box-sizing: border-box; }
  html, body { width: 1200px; height: 1200px; overflow: hidden; }
  body { background: var(--stage); font-family: "Montserrat", sans-serif; }

  .flyer {
    position: absolute; left: 190px; top: 29px;
    width: 820px; height: 1142px;
    background: var(--paper); overflow: hidden;
  }
  .flyer > * { position: absolute; }

  .quote-mark {
    font-family: "Montserrat", sans-serif; font-weight: 800;
    color: var(--quote-grey); font-size: 190px; line-height: 1;
  }
  .quote-open { left: 62px; top: 28px; }
  .quote-close { left: 330px; top: 585px; }

  .title-line { position: absolute; left: 72px; line-height: 1; white-space: nowrap; }
  .title-pilot { top: 142px; font-size: 90px; font-weight: 400; color: var(--red); }
  .title-grant { top: 222px; font-size: 90px; font-weight: 400; color: var(--red); }
  .title-application { top: 302px; font-size: 48px; font-weight: 700; color: var(--slate); letter-spacing: 0.5px; }
  .title-announcement { top: 361px; font-size: 40px; font-weight: 300; color: var(--slate); letter-spacing: 1px; }
  .title-year { top: 399px; font-size: 122px; font-weight: 200; color: var(--red); letter-spacing: -6px; }

  .intro {
    left: 72px; top: 537px;
    font-size: 23px; line-height: 29px; font-weight: 400; color: var(--ink);
    letter-spacing: 0.2px; white-space: nowrap;
  }
  .intro strong { color: var(--red); font-weight: 700; }

  .divider { left: 459px; top: 438px; width: 2px; height: 222px; background: #c9c9c9; }

  .key-dates { left: 483px; top: 437px; width: 330px; }
  .key-dates h2 {
    font-size: 21px; line-height: 26px; font-weight: 700; color: var(--red);
    letter-spacing: 0.3px;
  }
  .key-dates p { font-size: 23px; line-height: 29px; color: var(--ink); font-weight: 400; letter-spacing: 0.3px; }
  .key-dates .deadline p { margin-top: 10px; }
  .key-dates .funding { margin-top: 30px; }

  .brand {
    left: 512px; top: 108px; display: flex; align-items: center; gap: 12px;
    color: var(--blue-deep); font-weight: 600; font-size: 20px; line-height: 24px;
  }
  .brand-dot { width: 52px; height: 52px; border-radius: 50%; background: var(--blue-deep); flex: none; }

  .art-helix-faint {
    left: 420px; top: 40px; width: 400px; height: 620px;
    background: radial-gradient(ellipse 45% 50% at 70% 45%, rgba(205,208,212,0.45) 0%, rgba(220,222,226,0.25) 50%, rgba(255,255,255,0) 100%);
  }
  .art-helix-main {
    left: 0; top: 680px; width: 820px; height: 330px;
    background: linear-gradient(175deg, rgba(255,255,255,0) 10%, rgba(170,174,179,0.55) 45%, var(--silver) 70%, rgba(150,154,160,0.8) 100%);
  }

  .wave { left: 0; top: 900px; width: 820px; height: 242px; }

  .contact-title {
    left: 67px; top: 1022px; font-family: "Oswald", sans-serif; font-weight: 300;
    font-size: 24px; line-height: 1; color: var(--red); letter-spacing: 0.3px;
  }
  .contact-address, .contact-lines {
    font-family: "Lato", sans-serif; font-size: 14px; line-height: 17px; color: #fff;
    list-style: none;
  }
  .contact-address { left: 65px; top: 1052px; }
  .contact-address li { padding-left: 17px; position: relative; }
  .contact-lines { left: 555px; top: 1045px; line-height: 19px; }
  .contact-lines li { display: flex; align-items: center; gap: 8px; }
  .icon { width: 12px; height: 12px; flex: none; fill: #fff; }
  .contact-address .icon { position: absolute; left: 0; top: 2px; }
</style>
</head>
<body>
  <main class="flyer">
    <div class="art-helix-faint" role="img" aria-label="Faint grey DNA double helix rising to the top right"></div>
    <div class="art-helix-main" role="img" aria-label="Silver metallic DNA double helix running across the lower page"></div>

    <svg class="wave" viewBox="0 0 820 242" preserveAspectRatio="none" aria-hidden="true">
      <defs>
        <radialGradient id="band-glow" cx="0.5" cy="0.3" r="0.6">
          <stop offset="0" stop-color="#2a7ac0"/>
          <stop offset="1" stop-color="#124a8c"/>
        </radialGradient>
      </defs>
      <path d="M0 80 C120 60 200 20 320 50 C420 75 480 95 560 60 C650 25 740 30 820 40 L820 242 L0 242 Z" fill="url(#band-glow)"/>
    </svg>

    <div class="quote-mark quote-open" aria-hidden="true">&ldquo;</div>

    <div class="brand">
      <span class="brand-dot"></span>
      <span>Norvale<br>Cell Markers Institute</span>
    </div>

    <h1>
      <span class="title-line title-pilot">PILOT</span>
      <span class="title-line title-grant">GRANT</span>
      <span class="title-line title-application">APPLICATION</span>
      <span class="title-line title-announcement">ANNOUNCEMENT</span>
      <span class="title-line title-year">2018</span>
    </h1>

    <p class="intro">There are three pilot grants<br>that announced at the same<br>time next year on<br><strong>September 17, 2018</strong></p>
    <div class="quote-mark quote-close" aria-hidden="true">&rdquo;</div>

    <div class="divider"></div>

    <section class="key-dates">
      <div class="deadline">
        <h2>THE DEADLINE FOR<br>APPLICATIONS</h2>
        <p>October 31, 2018</p>
      </div>
      <div class="funding">
        <h2>THE FUNDING PERIOD<br>WILL BE FROM</h2>
        <p>November 12th, 2018 to<br>November 11, 2019.</p>
      </div>
    </section>

    <h3 class="contact-title">CONTACT US</h3>
    <ul class="contact-address">
      <li><svg class="icon" viewBox="0 0 12 12"><path d="M6 1 L11.5 6 L10 6 L10 11 L7 11 L7 8 L5 8 L5 11 L2 11 L2 6 L0.5 6 Z"/></svg>Cell Markers Institute</li>
      <li>9th Floor, Halden Center for Applied Biology</li>
      <li>1250 Riverside Park Way, Norvale, NV 20417</li>
    </ul>
    <ul class="contact-lines">
      <li><svg class="icon" viewBox="0 0 12 12"><path d="M2.5 1 L4.5 1 L5.5 3.5 L4.2 4.6 C4.8 5.9 6 7.1 7.4 7.8 L8.5 6.5 L11 7.5 L11 9.5 C11 10.4 10.3 11 9.5 11 C5 10.6 1.4 7 1 2.5 C1 1.7 1.6 1 2.5 1 Z"/></svg>555-014-2738</li>
      <li><svg class="icon" viewBox="0 0 12 12"><path d="M1 2.5 L11 2.5 L11 9.5 L1 9.5 Z M1.6 3 L6 6.5 L10.4 3" stroke="#124a8c" stroke-width="0.8"/></svg>grants@norvale.edu</li>
      <li><svg class="icon" viewBox="0 0 12 12"><circle cx="6" cy="6" r="5" fill="none" stroke="#fff" stroke-width="1.1"/><path d="M1 6 H11 M6 1 C3.5 3.5 3.5 8.5 6 11 C8.5 8.5 8.5 3.5 6 1" fill="none" stroke="#fff" stroke-width="0.9"/></svg>cellmarkers.sci.norvale.edu</li>
    </ul>
  </main>
</body>
</html>
```